Tallowbrook Fitness - Personal & Rehab Training

Business Card for my personal training business - Tallowbrook Fitness. I focus on personal and rehab training. I would like a double sided card, round edges. front of card will be my existing logo and the back will have an image (black and white or exercise, people exercising, weights, etc) along with my name and details. Such as:
Corisse Pembly
Personal & Rehab Trainer
www.tallowbrookfitness.com.au
0438264905
I have some images that I have downloaded that I am happy to send to the designer.
Thanks
Target Market(s)
athletes, middle to high income, sport related
Contact Information for Business Card
Corisse Pembly
Personal & Rehab Trainer
0438264905
Colors
Designer to choose only greyscale colors for use in the design.
Requirements
Must have
- my existing logo
Nice to have
- one of the images uploaded. I really like the girl with the mint coloured shoes as this is one of my logo colours

```html
<!DOCTYPE html>
<html lang="en">
<head>
<meta charset="utf-8">
<title>Tallowbrook Fitness – Business Card</title>
<link rel="stylesheet" href="https://fonts.googleapis.com/css2?family=Montserrat:wght@500;600;700&family=Lora:wght@400&display=swap">
<style>
  :root {
    --stage: #1d1e23;
    --ink: #111111;
    --paper: #ffffff;
    --ghost: #ececec;
    --photo-dark: #161616;
    --photo-mid: #4a4a4a;
    --photo-light: #8a8a8a;
    --mint: #4fd1c5;
    --rule: #222222;
  }
  * { box-sizing: border-box; margin: 0; padding: 0; }
  html, body { width: 1200px; height: 800px; overflow: hidden; background: var(--stage); }
  .stage {
    width: 1200px; height: 800px;
    display: flex; align-items: center; justify-content: center; gap: 40px;
  }
  .card {
    position: relative;
    width: 525px; height: 300px;
    border-radius: 22px;
    overflow: hidden;
  }

  /* Front: photo side */
  .card--photo { background: var(--photo-dark); }
  .photo-fill {
    position: absolute; inset: 0;
    background:
      radial-gradient(ellipse 38% 32% at 18% 78%, rgba(79,209,197,.55), transparent 70%),
      radial-gradient(ellipse 34% 28% at 84% 18%, rgba(79,209,197,.55), transparent 70%),
      radial-gradient(ellipse 40% 45% at 55% 60%, var(--photo-mid), transparent 75%),
      linear-gradient(160deg, var(--photo-light) 0%, var(--photo-mid) 35%, var(--photo-dark) 100%);
  }
  .brand {
    position: absolute;
    display: flex; align-items: center; gap: 16px;
  }
  .brand__square {
    width: 52px; height: 52px;
    border: 4px solid currentColor;
    border-radius: 9px;
    flex: none;
  }
  .brand__name {
    font-family: "Montserrat", sans-serif;
    font-weight: 600;
    font-size: 20px;
    letter-spacing: 3px;
    text-transform: uppercase;
    white-space: nowrap;
    line-height: 1;
    padding-bottom: 9px;
    border-bottom: 2px solid currentColor;
  }
  .card--photo .brand { color: var(--paper); left: 70px; top: 124px; }

  /* Back: details side */
  .card--details { background: var(--paper); color: var(--ink); }
  .ghost-square {
    position: absolute;
    left: -60px; top: 150px;
    width: 240px; height: 240px;
    border: 22px solid var(--ghost);
    border-radius: 40px;
  }
  .card--details .brand { left: 80px; top: 72px; }
  .card--details .brand__name { border-bottom-color: var(--rule); }
  .details {
    position: absolute;
    left: 80px; top: 176px;
    display: flex; align-items: center; gap: 14px;
  }
  .person { white-space: nowrap; }
  .person__name {
    font-family: "Montserrat", sans-serif;
    font-weight: 700;
    font-size: 16px;
    text-transform: uppercase;
    letter-spacing: .5px;
  }
  .person__role {
    font-family: "Lora", serif;
    font-size: 13px;
    margin-top: 3px;
  }
  .details__divider { width: 2px; height: 40px; background: var(--rule); flex: none; }
  .contact { list-style: none; font-family: "Lora", serif; font-size: 12px; white-space: nowrap; }
  .contact li { display: flex; align-items: center; gap: 7px; line-height: 20px; }
  .contact svg { width: 12px; height: 12px; flex: none; }
</style>
</head>
<body>
<main class="stage">
  <section class="card card--photo">
    <div class="photo-fill" role="img" aria-label="Black and white photo of an athlete in mint trainers lifting a kettlebell"></div>
    <div class="brand">
      <span class="brand__square"></span>
      <span class="brand__name">Tallowbrook Fitness</span>
    </div>
  </section>

  <section class="card card--details">
    <span class="ghost-square"></span>
    <div class="brand">
      <span class="brand__square"></span>
      <span class="brand__name">Tallowbrook Fitness</span>
    </div>
    <div class="details">
      <div class="person">
        <p class="person__name">Corisse Pembly</p>
        <p class="person__role">Personal &amp; Rehab Trainer</p>
      </div>
      <span class="details__divider"></span>
      <ul class="contact">
        <li>
          <svg viewBox="0 0 16 16" aria-hidden="true"><rect x="0.5" y="0.5" width="15" height="15" rx="2" fill="none" stroke="#111"/><path d="M4 5c0-1 1-1.5 2-1.5l1 2-1 1c.5 1.2 1.3 2 2.5 2.5l1-1 2 1c0 1-.5 2-1.5 2C6.5 11 4 8.5 4 5z" fill="#111"/></svg>
          0438264905
        </li>
        <li>
          <svg viewBox="0 0 16 16" aria-hidden="true"><rect x="0.5" y="0.5" width="15" height="15" rx="2" fill="none" stroke="#111"/><circle cx="8" cy="8" r="4.5" fill="none" stroke="#111"/><ellipse cx="8" cy="8" rx="2" ry="4.5" fill="none" stroke="#111"/><path d="M3.5 8h9" stroke="#111"/></svg>
          www.tallowbrookfitness.com.au
        </li>
      </ul>
    </div>
  </section>
</main>
</body>
</html>
```